Brindlewick Solutions - Website for a CRM IT Services Provider to Non-profits

We need a website design for our company that provides IT services to non-profits to enable them to manage their donors and philanthropy within their organization.

We would like to see a design that uses the colors in our logo and a funky take on how to uniquely present a topic as boring as IT. Examples of sites that we really like: tamsinvoke.com, www.corabellquist.com, mintgable.com

The final design should communicate that we are a professional, yet creative company that is fun to work with.

Target Market(s)

Non-profits who tend to be young, creative types that are low-tech

Industry/Entity Type

It Company

Requirements
Must have
• Must include tabs for Home, Contact Us, About, Projects, and Blog. The site must use the logo we have attached on all of the page, in one way or another (it can be small & in the corner).

The site has to work on all mobile browsers (iphone, ipad).
Nice to have
• It would be great if I could supply some HTML for the Contact page that would allow me to capture leads and put them directly into my CRM application. It's very easy to set up.
Should not have
• The design should not use old-style fonts and should not have a lot of dark colors. Keep it similar to our logo, clean and simple. We're not looking for a busy home page.

```html
<!DOCTYPE html>
<html lang="en">
<head>
<meta charset="utf-8">
<title>Brindlewick Solutions — Home</title>
<link rel="stylesheet" href="https://fonts.googleapis.com/css2?family=Didact+Gothic&family=Oswald:wght@700&family=Caveat:wght@600&display=swap">
<style>
  :root {
    --sea: #3898ad;
    --sea-deep: #2a8198;
    --glow: #6fe8ec;
    --headline: #1f5d6d;
    --nav-text: #1d5667;
    --nav-active: #1f6d82;
    --white: #ffffff;
    --footer: #1f6f86;
    --footer-soft: #2b7f95;
    --logo-disc: #d9f4f1;
    --muted: #a9d3dd;
  }
  * { box-sizing: border-box; margin: 0; padding: 0; }
  html, body { width: 1200px; height: 1015px; overflow: hidden; }
  body {
    position: relative;
    font-family: "Didact Gothic", sans-serif;
    background:
      radial-gradient(ellipse 520px 260px at 600px 0, var(--glow) 0%, rgba(111,232,236,0.35) 55%, rgba(111,232,236,0) 100%),
      radial-gradient(ellipse 700px 500px at 600px 380px, #4fa9bd 0%, var(--sea) 60%, var(--sea-deep) 100%);
  }
  .brand { position: absolute; left: 218px; top: 25px; width: 84px; text-align: center; }
  .brand-disc { width: 84px; height: 84px; border-radius: 50%; background: var(--logo-disc); }
  .brand-name { margin-top: 6px; color: var(--white); font-size: 13px; white-space: nowrap; margin-left: -20px; margin-right: -20px; }

  .main-nav { position: absolute; top: 54px; left: 430px; }
  .main-nav a {
    display: block; height: 36px; line-height: 37px; font-size: 15px; letter-spacing: 2px;
    color: var(--nav-text); text-decoration: none; text-transform: uppercase; position: absolute; white-space: nowrap;
  }
  .main-nav a.active { background: var(--nav-active); color: var(--white); width: 64px; text-align: center; left: 0; }

  .headline {
    position: absolute; left: 288px; top: 180px;
    font-family: "Oswald", sans-serif; font-weight: 700; font-size: 66px; line-height: 92px;
    color: var(--headline); text-transform: uppercase; letter-spacing: -1.5px;
  }
  .tablet {
    position: absolute; left: 598px; top: 187px; width: 323px; height: 261px;
    border-radius: 16px; background: linear-gradient(160deg, #2a2a2a, #0d0d0d);
    box-shadow: 0 4px 10px rgba(0,0,0,0.25);
  }
  .tablet-screen {
    position: absolute; left: 30px; top: 29px; width: 262px; height: 204px;
    background: linear-gradient(180deg, #f4f6f8, #e4e9ee);
  }
  .tagline {
    position: absolute; left: 0; width: 1172px; top: 496px; text-align: center;
    color: var(--white); font-size: 30px; line-height: 36px; letter-spacing: 2.6px;
  }
  .reef {
    position: absolute; left: 200px; top: 640px; width: 760px; height: 170px;
    background: radial-gradient(ellipse 380px 120px at 50% 70%, rgba(120,200,215,0.35), rgba(120,200,215,0));
  }
  .footer-band { position: absolute; left: 0; top: 780px; width: 1200px; height: 235px; }
  .footer-mark { position: absolute; left: 235px; top: 812px; width: 52px; height: 52px; border-radius: 50%; background: var(--footer-soft); }
  .copyright { position: absolute; left: 234px; top: 870px; font-family: Arial, sans-serif; font-size: 10px; color: var(--muted); }
  .connect { position: absolute; left: 846px; top: 824px; font-family: "Caveat", cursive; font-size: 15px; color: var(--white); letter-spacing: 1px; }
  .social { position: absolute; top: 850px; width: 30px; height: 30px; border-radius: 50%; }
  .social.one { left: 858px; background: #4b6fa6; }
  .social.two { left: 896px; background: #47b4dc; }
</style>
</head>
<body>
  <header>
    <div class="brand">
      <div class="brand-disc"></div>
      <div class="brand-name">Brindlewick Solutions</div>
    </div>
    <nav class="main-nav">
      <a class="active" href="#">Home</a>
      <a href="#" style="left:92px">Contact Us</a>
      <a href="#" style="left:230px">About</a>
      <a href="#" style="left:320px">Projects</a>
      <a href="#" style="left:436px">Blog</a>
    </nav>
  </header>

  <main>
    <h1 class="headline">Measure<br>What<br>Matters</h1>
    <div class="tablet" role="img" aria-label="Tablet displaying a sales executive analytics dashboard">
      <div class="tablet-screen"></div>
    </div>
    <p class="tagline">Real-time analytics turn data into<br>information that enable your organization<br>to make critical decisions.</p>
    <div class="reef" role="img" aria-label="Faint seaweed and bubble decoration"></div>
  </main>

  <footer>
    <svg class="footer-band" viewBox="0 0 1200 235" preserveAspectRatio="none" aria-hidden="true">
      <path fill="var(--footer)" d="M0 40 Q30 5 70 25 Q120 0 170 30 Q230 10 290 35 Q360 5 420 30 Q470 15 520 25 Q570 -5 620 20 Q680 0 740 30 Q790 10 840 30 Q890 -10 950 20 Q1010 -5 1060 25 Q1120 5 1160 20 Q1185 25 1200 18 L1200 235 L0 235 Z"/>
    </svg>
    <div class="footer-mark"></div>
    <p class="copyright">copyright 2012</p>
    <p class="connect">CONNECT WITH US</p>
    <a class="social one" href="#" aria-label="Social profile"></a>
    <a class="social two" href="#" aria-label="Social feed"></a>
  </footer>
</body>
</html>
```